We need a web site design that is connected to Ridgeway Roofing an American company, Veteran owned. Specializing in new roofs of all kinds, repair existing roofs and emergency roof repairs. located in the north Georgia mountains

Target Market(s)

homeowners end users, real estate, home owners insurance companies

Industry/Entity Type

roofing

Contact Information for Business Card

logo, Veteran owned, supports veteran charities, phone number ect

Font styles to use
Serif

Requirements
Should not have
• na

```html
<!DOCTYPE html>
<html lang="en">
<head>
<meta charset="utf-8">
<title>Ridgeway Roofing – Business Card</title>
<link rel="stylesheet" href="https://fonts.googleapis.com/css2?family=Libre+Baskerville:wght@700&family=Source+Serif+4:wght@400;600&display=swap">
<style>
  :root {
    --backdrop: #2a2a2a;
    --navy: #1f5a8f;
    --paper: #ffffff;
    --ink: #1c1c1c;
    --brand-blue: #1d4f8c;
    --accent-red: #e2262a;
    --rule: #8a8a8a;
    --muted: #2b2b2b;
    --soft-white: rgba(255, 255, 255, 0.85);
  }
  * { margin: 0; padding: 0; box-sizing: border-box; }
  html, body { width: 1200px; height: 800px; overflow: hidden; }
  body {
    background: var(--backdrop);
    font-family: "Source Serif 4", Georgia, serif;
    position: relative;
  }
  .card {
    position: absolute;
    top: 250px;
    width: 520px;
    height: 300px;
    border-radius: 18px;
    overflow: hidden;
  }
  .card-front { left: 50px; background: var(--navy); }
  .card-back  { left: 630px; background: var(--paper); }

  .services {
    position: absolute;
    top: 30px;
    right: 34px;
    list-style: none;
    text-align: right;
    color: var(--paper);
    font-size: 15px;
    line-height: 1.5;
  }
  .brand-name {
    font-family: "Libre Baskerville", Georgia, serif;
    font-weight: 700;
    text-transform: uppercase;
    letter-spacing: 0.5px;
    white-space: nowrap;
  }
  .card-front .brand-name {
    position: absolute;
    right: 34px;
    bottom: 62px;
    color: var(--paper);
    font-size: 20px;
  }
  .front-tagline {
    position: absolute;
    right: 34px;
    bottom: 38px;
    color: var(--soft-white);
    font-size: 13px;
    letter-spacing: 1.5px;
    text-transform: uppercase;
  }
  .back-brand {
    position: absolute;
    left: 0;
    top: 168px;
    width: 252px;
    text-align: center;
  }
  .card-back .brand-name { color: var(--ink); font-size: 17px; }
  .veteran-note {
    margin-top: 8px;
    font-size: 12.5px;
    line-height: 1.4;
    color: var(--muted);
  }
  .veteran-note strong { color: var(--accent-red); font-weight: 600; }
  .divider {
    position: absolute;
    left: 252px;
    top: 50px;
    width: 1px;
    height: 200px;
    background: var(--rule);
  }
  .details {
    position: absolute;
    left: 280px;
    top: 64px;
    color: var(--muted);
  }
  .person-name {
    font-family: "Libre Baskerville", Georgia, serif;
    font-weight: 700;
    font-size: 19px;
    color: var(--brand-blue);
    letter-spacing: 0.3px;
    text-transform: uppercase;
  }
  .person-role { font-size: 15px; margin-top: 3px; margin-bottom: 14px; }
  .contact-list { list-style: none; font-size: 14px; line-height: 1.35; }
  .contact-list li { display: flex; align-items: flex-start; gap: 8px; margin-bottom: 3px; }
  .contact-list svg { flex: none; margin-top: 3px; }
</style>
</head>
<body>
  <section class="card card-front" aria-label="Card front">
    <ul class="services">
      <li>• New Roofs &nbsp;•&nbsp; Repair Existing Roofs</li>
      <li>• Emergency Roof Repairs</li>
    </ul>
    <p class="brand-name">Ridgeway Roofing</p>
    <p class="front-tagline">Veteran Owned</p>
  </section>

  <section class="card card-back" aria-label="Card back">
    <div class="back-brand">
      <p class="brand-name">Ridgeway Roofing</p>
      <p class="veteran-note"><strong>Veteran Owned</strong><br>Supports Veteran Charities</p>
    </div>
    <div class="divider"></div>
    <div class="details">
      <h1 class="person-name">Daniel Harper</h1>
      <p class="person-role">Founder &amp; Director</p>
      <ul class="contact-list">
        <li>
          <svg width="12" height="12" viewBox="0 0 12 12" aria-hidden="true"><rect x="1.5" y="1.5" width="9" height="9" rx="2" fill="none" stroke="var(--accent-red)" stroke-width="1.6"/></svg>
          <span>044-321 654 987</span>
        </li>
        <li>
          <svg width="12" height="12" viewBox="0 0 12 12" aria-hidden="true"><path d="M1 6 L11 1 L8 11 L6 7 Z" fill="var(--accent-red)"/></svg>
          <span>hello@ridgewayroof.com</span>
        </li>
        <li>
          <svg width="12" height="13" viewBox="0 0 12 13" aria-hidden="true"><path d="M6 12 C3 8 1.5 6.5 1.5 4.6 A4.5 4.5 0 0 1 10.5 4.6 C10.5 6.5 9 8 6 12 Z" fill="none" stroke="var(--accent-red)" stroke-width="1.6"/><circle cx="6" cy="4.6" r="1.4" fill="var(--accent-red)"/></svg>
          <span>4417 Laurel Creek Pkwy<br>210-B, GA 30512</span>
        </li>
      </ul>
    </div>
  </section>
</body>
</html>
```